Brell Harbor Company Business Cards

Front and Back Business Card - logo and text setup - cool design. I need workable photoshop or illustrator files so I can setup each employee card with design that is created
Updates

Hi everyone, thank you for the great entries. Please no more white and blue cards - there are so many already - black and silver only now please. thanks!

Target Market(s)

Construction Industry - Facility Managers

Industry/Entity Type

Construction

Contact Information for Business Card

I really like contemporary simplistic looks - clean neat....not opposed to seeing some black backrounds

Requirements
Must have
• Logo/website address with design on front only - www.brellharbor-example.com (logo attached)
• Back:
• Name/Title/Company Address/Phone/email address
Nice to have
• Cool design
Should not have
• Nothing gimmicky like Fire or Water - since we are a Fire Protection company - it has all been done

```html
<!DOCTYPE html>
<html lang="en">
<head>
<meta charset="utf-8">
<title>Brell Harbor Company – Business Cards</title>
<link rel="stylesheet" href="https://fonts.googleapis.com/css2?family=Montserrat:wght@400;500;700;800&display=swap">
<style>
  :root {
    --backdrop: #e3e5e7;
    --card: #fbfbfb;
    --ink: #1b1c1e;
    --charcoal: #3a3d42;
    --silver: #b4b8be;
    --silver-dark: #7d8288;
    --white: #ffffff;
  }
  * { box-sizing: border-box; margin: 0; padding: 0; }
  html, body { width: 1200px; height: 969px; overflow: hidden; }
  body {
    background: var(--backdrop);
    font-family: "Montserrat", Arial, sans-serif;
    position: relative;
  }
  .card {
    position: absolute;
    width: 500px;
    height: 290px;
    background: var(--card);
    box-shadow: 0 6px 18px rgba(0,0,0,0.12);
    overflow: hidden;
  }
  .card-front { left: 90px; top: 170px; }
  .card-back { left: 610px; top: 500px; }
  .card-shapes { position: absolute; inset: 0; width: 100%; height: 100%; }

  .brand-name {
    position: absolute;
    color: var(--ink);
    font-weight: 800;
    letter-spacing: -0.02em;
    line-height: 1;
    white-space: nowrap;
  }
  .card-front .brand-name { left: 70px; top: 118px; font-size: 54px; }
  .card-back .brand-name { right: 28px; top: 38px; font-size: 26px; }

  .front-web {
    position: absolute;
    left: 74px;
    top: 186px;
    color: var(--silver-dark);
    font-size: 14px;
    font-weight: 500;
    letter-spacing: 0.06em;
  }

  .person { position: absolute; left: 24px; top: 72px; }
  .person-name { color: var(--ink); font-size: 19px; font-weight: 400; letter-spacing: 0.02em; }
  .person-name strong { font-weight: 700; }
  .person-title { color: var(--silver-dark); font-size: 13px; font-weight: 500; letter-spacing: 0.06em; margin-top: 4px; }

  .contact-row {
    position: absolute;
    left: 22px;
    display: flex;
    align-items: center;
    gap: 12px;
    color: var(--white);
    font-size: 12.5px;
    font-weight: 500;
    letter-spacing: 0.05em;
    line-height: 1.25;
  }
  .contact-row.address { top: 153px; }
  .contact-row.phone { top: 207px; }
  .contact-row.email { top: 234px; }
  .contact-row.web { top: 261px; }
  .contact-icon {
    flex: none;
    width: 22px;
    height: 22px;
    border-radius: 50%;
    background: var(--white);
    display: flex;
    align-items: center;
    justify-content: center;
  }
  .contact-icon svg { width: 13px; height: 13px; }
</style>
</head>
<body>

<section class="card card-front" aria-label="Business card front">
  <svg class="card-shapes" viewBox="0 0 500 290" aria-hidden="true">
    <polygon points="0,0 330,0 0,120" fill="var(--charcoal)"/>
    <polygon points="250,0 390,0 310,28 210,28" fill="var(--silver)"/>
    <polygon points="500,150 500,290 260,290" fill="var(--ink)"/>
    <polygon points="150,290 300,230 330,290" fill="var(--silver)"/>
  </svg>
  <div class="brand-name">brell harbor</div>
  <p class="front-web">WWW.BRELLHARBOR-EXAMPLE.COM</p>
</section>

<section class="card card-back" aria-label="Business card back">
  <svg class="card-shapes" viewBox="0 0 500 290" aria-hidden="true">
    <polygon points="290,0 500,0 500,12 330,22" fill="var(--silver)"/>
    <polygon points="0,145 270,145 320,198 0,198" fill="var(--ink)"/>
    <polygon points="0,198 320,198 370,168 400,168 490,290 0,290" fill="var(--charcoal)"/>
  </svg>

  <div class="brand-name">brell harbor</div>

  <div class="person">
    <p class="person-name">NAME <strong>SURNAME</strong></p>
    <p class="person-title">MANAGER</p>
  </div>

  <div class="contact-row address">
    <span class="contact-icon"><svg viewBox="0 0 16 16"><path d="M8 2 1 8h2v6h4v-4h2v4h4V8h2z" fill="var(--ink)"/></svg></span>
    <span>ADDRESS GOES HERE<br>CITY, COUNTRY, ZIPCODE</span>
  </div>
  <div class="contact-row phone">
    <span class="contact-icon"><svg viewBox="0 0 16 16"><path d="M4 1.5 6 4.5 4.8 6.2a8 8 0 0 0 5 5L11.5 10l3 2-1.3 2.4C7 14.5 1.5 9 1.6 2.8z" fill="var(--ink)"/></svg></span>
    <span>+00 123 456 789</span>
  </div>
  <div class="contact-row email">
    <span class="contact-icon"><svg viewBox="0 0 16 16"><rect x="1.5" y="3.5" width="13" height="9" fill="none" stroke="var(--ink)" stroke-width="1.6"/><path d="M1.5 3.5 8 9l6.5-5.5" fill="none" stroke="var(--ink)" stroke-width="1.6"/></svg></span>
    <span>NAME@BRELLHARBOR-EXAMPLE.COM</span>
  </div>
  <div class="contact-row web">
    <span class="contact-icon"><svg viewBox="0 0 16 16"><circle cx="8" cy="8" r="6.3" fill="none" stroke="var(--ink)" stroke-width="1.5"/><ellipse cx="8" cy="8" rx="2.6" ry="6.3" fill="none" stroke="var(--ink)" stroke-width="1.2"/><path d="M1.7 8h12.6" stroke="var(--ink)" stroke-width="1.2"/></svg></span>
    <span>WWW.BRELLHARBOR-EXAMPLE.COM</span>
  </div>
</section>

</body>
</html>
```